Magazine advertisement for wedding proposal

SPECS
Page size: 221,0-290,0
File format:Certified PDF PrintSpec_7Q2 (CMYK).
supply with crop marks on sheet mirror format
boundlessly knitted

CONTENT
I am going to ask my wife to marry me (again). I have bought a 1/1 page in her favourite Glossy. I would like the advertisement to present a letter from a type machine covered with some polaroid pictures of her. Idea is to mimic a guy in love writing a letter and dreaming away at her pictures. I would like the whole look and feel to be professional and in style. As such colours etc. may be changed and altered to make it a great integrated piece. I have added multiple pohoto's. Not all have to be used. You can choose which and how much you find most appealing. I At least want Photo Noor 1 to be used and one of the pictures with us together in white (couple).

The letter should read the following text:

Once in your lifetime you meet someone who changes everything.
She is going to do her thing with or without you. That's why she is a queen.

But we are just better together, babe...☺
That's why I want you to love me, stay with me and marry me. Would you?

Fenna,

Wil je met me trouwen?

-xxx-

Wouter

Requirements
Must have
• Be creative! This is just my first thought, but if you have an idea which you think is better, please let me know.
• - light & warm colours which all have the same look and feel (I do not like too much accent and opposite colours)
• - text as a love letter or poem
• - usage of Photo Noor 1
• - usage of couple photo
• - usage of both photo's with kids
Should not have
• - too cliché props - one or two things like hearts and flowers is ok, but dont overdo it

```html
<!DOCTYPE html>
<html lang="nl">
<head>
<meta charset="utf-8">
<title>Proposal advertisement</title>
<link rel="stylesheet" href="https://fonts.googleapis.com/css2?family=Raleway:ital,wght@0,500;0,600;1,500&family=Open+Sans:wght@700&display=swap">
<style>
  :root {
    --backdrop: #d9dadb;
    --paper: #f2f3f5;
    --ink: #2f3133;
    --ink-soft: #3b3d40;
    --sky-top: #5e7e9f;
    --sky-bottom: #b9c7d3;
    --sun-warm: #c9b08f;
    --sun-light: #e6d7c0;
    --pool-blue: #58b7d6;
    --float-red: #d9484a;
    --skin-warm: #d8b497;
    --skin-light: #efd9c4;
  }
  * { box-sizing: border-box; margin: 0; padding: 0; }
  html, body {
    width: 1200px; height: 862px; overflow: hidden;
    background: var(--backdrop);
  }
  .page {
    position: absolute; left: 295px; top: 31px;
    width: 610px; height: 800px;
    background: var(--paper);
    box-shadow: 0 6px 24px rgba(0,0,0,.18);
    font-family: "Raleway", sans-serif;
    color: var(--ink);
  }
  .photo { position: absolute; }
  .photo--couple {
    left: 24px; top: 24px; width: 360px; height: 290px;
    background: linear-gradient(180deg, var(--sky-top), var(--sky-bottom));
  }
  .photo--pool {
    left: 24px; top: 322px; width: 360px; height: 172px;
    background: linear-gradient(180deg, #6d8a5a 0%, var(--pool-blue) 55%, var(--float-red) 100%);
  }
  .photo--sun-hat {
    left: 392px; top: 24px; width: 194px; height: 205px;
    background: linear-gradient(160deg, var(--sun-light), var(--sun-warm));
  }
  .photo--embrace {
    left: 392px; top: 237px; width: 194px; height: 257px;
    background: linear-gradient(170deg, var(--skin-light), var(--skin-warm));
  }
  .letter {
    position: absolute; left: 30px; top: 520px; width: 556px;
    font-size: 14px; line-height: 1.5; font-weight: 600; color: var(--ink-soft);
  }
  .letter p + p { margin-top: 14px; }
  .letter .salutation { font-weight: 500; font-style: italic; }
  .question {
    position: absolute; left: 30px; top: 668px;
    font-size: 30px; font-weight: 500; color: var(--ink);
  }
  .signature {
    position: absolute; left: 400px; top: 724px;
    font-family: "Open Sans", sans-serif; font-weight: 700;
    font-size: 38px; color: var(--ink);
  }
</style>
</head>
<body>
  <article class="page">
    <div class="photo photo--couple" role="img" aria-label="Couple dressed in white embracing against a blue sky"></div>
    <div class="photo photo--pool" role="img" aria-label="Woman relaxing on a red pool float"></div>
    <div class="photo photo--sun-hat" role="img" aria-label="Mother in sunglasses with laughing toddler in a sun hat"></div>
    <div class="photo photo--embrace" role="img" aria-label="Smiling mother hugging a blond child"></div>

    <section class="letter">
      <p>Once in your lifetime you meet someone who changes everything. She is going to do her thing with or without you. That’s why she is a queen.</p>
      <p>But we are just better together, babe…<br>That’s why I want you to love me, stay with me and marry me. Would you?</p>
      <p class="salutation">Fenna,</p>
    </section>

    <h1 class="question">Wil je met me trouwen?</h1>
    <p class="signature">Wouter</p>
  </article>
</body>
</html>
```